Business Card Design for a Handbags business

We are modernising our handbags website (see attached file for new front page) and are in need of a modern business card and a related design we can use on a small marquee at the markets, on letterhead, emails etc.

As the leather handbags we mostly import are from Italy, we want a smart modern European feel to the design. We are currently thinking about changing the name of the business from Larkmoor Handbags (see www.larkmoorhandbags.com.au) to Vintessa Handbags. Also open to other suggestions you may have that communicates the European influence and quality.

Target Market(s)

25-65 year old women (and some men)

Industry/Entity Type

Business

Contact Information for Business Card

Single or double sided - whichever creates more of an impact

Font styles to use
Serif
Sans Serif

Requirements
Must have
• Clean crisp look, slightly Italian or European look and feel to reflect where the handbags are imported from
Nice to have
• open to ideas

```html
<!DOCTYPE html>
<html lang="en">
<head>
<meta charset="utf-8">
<title>Vintessa Handbags – Business Card</title>
<link href="https://fonts.googleapis.com/css2?family=Lora:wght@400;700&display=swap" rel="stylesheet">
<style>
  :root {
    --page-bg: #d9d6d2;
    --card-white: #ffffff;
    --ink: #0b0b0b;
    --band-black: #000000;
    --band-text: #ffffff;
  }
  * { margin: 0; padding: 0; box-sizing: border-box; }
  html, body {
    width: 1200px;
    height: 902px;
    overflow: hidden;
  }
  body {
    background: var(--page-bg);
    font-family: "Lora", Georgia, serif;
    color: var(--ink);
  }
  .business-card {
    position: absolute;
    left: 100px;
    top: 166px;
    width: 1000px;
    height: 570px;
    background: var(--card-white);
    display: flex;
    flex-direction: column;
    box-shadow: 0 10px 30px rgba(0,0,0,0.18);
  }
  .card-header {
    height: 229px;
    display: flex;
    justify-content: space-between;
    padding: 40px 46px 0 47px;
  }
  .business-name {
    font-weight: 700;
    font-size: 50px;
    line-height: 58px;
    letter-spacing: 0.3px;
  }
  .contact-block {
    text-align: right;
    padding-top: 4px;
  }
  .contact-name {
    font-weight: 700;
    font-size: 34px;
    line-height: 42px;
  }
  .contact-phone {
    font-size: 26px;
    line-height: 36px;
    letter-spacing: 0.5px;
  }
  .contact-city {
    font-size: 26px;
    line-height: 36px;
    margin-top: 22px;
  }
  .rule-black { height: 6px; background: var(--band-black); }
  .rule-white { height: 6px; background: var(--card-white); }
  .photo-strip {
    height: 236px;
    display: flex;
    gap: 5px;
    background: var(--band-black);
  }
  .photo-panel { flex: 1; }
  .photo-green-clutch { background: linear-gradient(160deg, #8a7a6a 0%, #1c1c1c 45%, #1f7a3c 60%, #141414 100%); }
  .photo-quilted-bag { background: linear-gradient(160deg, #5f6b4e 0%, #9a9a98 40%, #1b1f2c 70%, #c9c7c2 100%); }
  .photo-red-tote { background: linear-gradient(160deg, #e4e2dc 0%, #5a5b42 40%, #c81818 65%, #4c4a3a 100%); }
  .photo-peach-tote { background: linear-gradient(160deg, #b39879 0%, #e59b7f 45%, #d9886b 70%, #1a1a1a 100%); }
  .web-band {
    flex: 1;
    background: var(--band-black);
    color: var(--band-text);
    display: flex;
    align-items: center;
    justify-content: center;
    font-size: 25px;
    letter-spacing: 0.6px;
  }
</style>
</head>
<body>
  <article class="business-card">
    <header class="card-header">
      <h1 class="business-name">Vintessa Handbags<br>&amp; Accessories</h1>
      <div class="contact-block">
        <p class="contact-name">Claudia Renner</p>
        <p class="contact-phone">0412 555 019</p>
        <p class="contact-city">Brisbane</p>
      </div>
    </header>
    <div class="rule-black"></div>
    <section class="photo-strip">
      <div class="photo-panel photo-green-clutch" role="img" aria-label="Photo of a woman in black holding a green leather clutch"></div>
      <div class="photo-panel photo-quilted-bag" role="img" aria-label="Photo of a woman in a leather jacket seated on steps with a black quilted bag"></div>
      <div class="photo-panel photo-red-tote" role="img" aria-label="Photo of a woman in a green knit holding a red leather tote"></div>
      <div class="photo-panel photo-peach-tote" role="img" aria-label="Photo of a peach suede tote bag carried by a woman"></div>
    </section>
    <div class="rule-black"></div>
    <div class="rule-white"></div>
    <footer class="web-band">www.vintessahandbags.com.au</footer>
  </article>
</body>
</html>
```